Now Leasing Banner

Looking for a banner that says the following information approx 4' x 30'

Now Leasing Maple Ridge Court 925-318-6042

Target Market(s)

Drive by traffic

Industry/Entity Type

Residential property management

Requirements
Must have
• Clear and readable from a distance

```html
<!DOCTYPE html>
<html lang="en">
<head>
<meta charset="utf-8">
<title>Now Leasing – Maple Ridge Court</title>
<link rel="stylesheet" href="https://fonts.googleapis.com/css2?family=Tinos:wght@700&display=swap">
<style>
  :root {
    --page-bg: #ffffff;
    --banner-red: #a10500;
    --banner-white: #ffffff;
    --headline-yellow: #f2f50c;
    --phone-shadow: #1a1a1a;
    --drop-shadow: rgba(0, 0, 0, 0.45);
  }
  html, body {
    margin: 0;
    padding: 0;
    width: 1200px;
    height: 213px;
    overflow: hidden;
    background: var(--page-bg);
  }
  .banner {
    display: block;
    width: 1200px;
    height: 213px;
  }
  .banner-text {
    font-family: "Tinos", "Times New Roman", serif;
    font-weight: 700;
  }
  .headline { fill: var(--headline-yellow); font-size: 70px; }
  .property-name { fill: var(--banner-white); font-size: 60px; }
  .phone { fill: var(--banner-red); font-size: 104px; }
  .phone-shadow { fill: var(--phone-shadow); font-size: 104px; }
  .panel-red { fill: var(--banner-red); }
  .panel-white { fill: var(--banner-white); }
  .banner-shadow { fill: var(--drop-shadow); }
</style>
</head>
<body>
<svg class="banner" viewBox="0 0 1200 213" xmlns="http://www.w3.org/2000/svg" aria-labelledby="banner-title">
  <title id="banner-title">Now Leasing Maple Ridge Court 925-318-6042</title>
  <defs>
    <filter id="soft-shadow" x="-5%" y="-30%" width="110%" height="160%">
      <feGaussianBlur stdDeviation="4"/>
    </filter>
  </defs>

  <rect class="banner-shadow" x="36" y="38" width="1152" height="154" filter="url(#soft-shadow)"/>
  <rect class="panel-white" x="29" y="29" width="1152" height="154"/>
  <rect class="panel-red" x="29" y="29" width="543" height="154"/>

  <g class="banner-text">
    <text class="headline" x="51" y="104" textLength="502" lengthAdjust="spacingAndGlyphs">NOW LEASING</text>
    <text class="property-name" x="98" y="166" textLength="410" lengthAdjust="spacingAndGlyphs">Maple Ridge Court</text>

    <text class="phone-shadow" x="593" y="148" textLength="572" lengthAdjust="spacingAndGlyphs">925-318-6042</text>
    <text class="phone" x="590" y="145" textLength="572" lengthAdjust="spacingAndGlyphs">925-318-6042</text>
  </g>
</svg>
</body>
</html>
```